Business Card Design

Dune Tanning Studio is a upmarket privately owned tanning and beauty salon. my card must look stylish. please also add appointment on back and facebook and instagram logos.

Industry/Entity Type

Business

Contact Information for Business Card

Dune Tanning Studio Pty Ltd
Solariums, Spray Tanning, Waxing & Eyelash Extensions
Shop 7-218 Carrow Bend Rd, Carrow Bend 4390
47619254

```html
<!DOCTYPE html>
<html lang="en">
<head>
<meta charset="utf-8">
<title>Dune Tanning Studio — Business Card</title>
<link href="https://fonts.googleapis.com/css2?family=Arimo:wght@400;700&display=swap" rel="stylesheet">
<style>
  :root {
    --teal: #1ba6ae;
    --teal-dark: #138990;
    --white: #ffffff;
    --grey: #8a8f93;
    --frame: #c9cdd0;
    --backdrop: #e4e6e7;
  }
  * { box-sizing: border-box; margin: 0; padding: 0; }
  html, body { width: 1200px; height: 900px; overflow: hidden; }
  body {
    background: var(--backdrop);
    font-family: "Arimo", Arial, sans-serif;
    position: relative;
  }
  .card {
    position: absolute;
    box-shadow: 0 6px 18px rgba(0,0,0,0.18);
  }

  /* Front */
  .card-front {
    left: 120px; top: 152px;
    width: 340px; height: 595px;
    background: var(--teal);
    color: var(--white);
    text-align: center;
    padding: 24px 22px;
  }
  .logo-panel {
    background: var(--white);
    border: 3px solid var(--frame);
    height: 210px;
    display: flex; align-items: center; justify-content: center; gap: 10px;
  }
  .logo-dot { width: 18px; height: 18px; border-radius: 50%; background: var(--teal); flex: none; }
  .logo-name { font-size: 21px; color: var(--grey); font-weight: 400; }
  .holder-name { margin-top: 40px; font-size: 22px; font-weight: 700; letter-spacing: 0.5px; }
  .holder-role { font-size: 14px; letter-spacing: 1px; margin-top: 3px; }
  .rule { width: 200px; height: 1px; background: var(--white); margin: 16px auto; }
  .company { font-size: 16px; font-weight: 700; }
  .address, .phone { font-size: 14px; line-height: 1.35; }
  .services-title { font-size: 14px; margin-bottom: 4px; }
  .services { font-size: 14px; line-height: 1.35; }

  /* Back */
  .card-back {
    left: 520px; top: 280px;
    width: 595px; height: 340px;
    background: var(--white);
    color: var(--teal);
    padding: 30px 0 0;
    text-align: center;
  }
  .appt-title { font-size: 19px; font-weight: 700; letter-spacing: 0.5px; }
  .appt-name { font-size: 15px; margin: 18px 0 22px; }
  .appt-list { list-style: none; width: 330px; margin: 0 auto; text-align: left; font-size: 14px; }
  .appt-list li { margin-bottom: 8px; white-space: nowrap; }
  .blank { display: inline-block; border-bottom: 1px solid var(--teal); height: 12px; vertical-align: baseline; }
  .social { display: flex; justify-content: center; gap: 5px; margin-top: 14px; }
  .social span { width: 20px; height: 20px; background: var(--teal); border-radius: 3px; }
</style>
</head>
<body>
  <section class="card card-front">
    <div class="logo-panel">
      <span class="logo-dot"></span>
      <span class="logo-name">Dune Tanning Studio</span>
    </div>
    <h1 class="holder-name">CLARA WHITFIELD</h1>
    <p class="holder-role">MANAGER</p>
    <div class="rule"></div>
    <p class="company">Dune Tanning Studio Pty Ltd</p>
    <p class="address">Shop 7-218 Carrow Bend Rd<br>Carrow Bend 4390</p>
    <p class="phone">[T] 47619254</p>
    <div class="rule"></div>
    <p class="services-title">- Services -</p>
    <p class="services">Solariums | Spray Tanning | Waxing<br>Eyelash Extensions</p>
  </section>

  <section class="card card-back">
    <h2 class="appt-title">YOUR APPOINTMENT</h2>
    <p class="appt-name">Name <span class="blank" style="width:150px"></span></p>
    <ol class="appt-list">
      <li>1. <span class="blank" style="width:34px"></span>am/pm <span class="blank" style="width:105px"></span> <span class="blank" style="width:22px"></span>/ <span class="blank" style="width:22px"></span>/ <span class="blank" style="width:22px"></span></li>
      <li>2. <span class="blank" style="width:34px"></span>am/pm <span class="blank" style="width:105px"></span> <span class="blank" style="width:22px"></span>/ <span class="blank" style="width:22px"></span>/ <span class="blank" style="width:22px"></span></li>
      <li>3. <span class="blank" style="width:34px"></span>am/pm <span class="blank" style="width:105px"></span> <span class="blank" style="width:22px"></span>/ <span class="blank" style="width:22px"></span>/ <span class="blank" style="width:22px"></span></li>
      <li>4. <span class="blank" style="width:34px"></span>am/pm <span class="blank" style="width:105px"></span> <span class="blank" style="width:22px"></span>/ <span class="blank" style="width:22px"></span>/ <span class="blank" style="width:22px"></span></li>
      <li>5. <span class="blank" style="width:34px"></span>am/pm <span class="blank" style="width:105px"></span> <span class="blank" style="width:22px"></span>/ <span class="blank" style="width:22px"></span>/ <span class="blank" style="width:22px"></span></li>
    </ol>
    <div class="social" aria-label="Social media links">
      <span></span><span></span><span></span>
    </div>
  </section>
</body>
</html>
```